Fitness Tracker for Fitness Club

We need a graphic design for a fitness app.

The app will display videos of live workouts, provide the ability to communicate to a trainer through an inbox, and the ability to track weight over time.

The layout provided is the current demo mobile html application, we would like to change this to a custom app and would like a new design, something that is clean and current. Something like kinora feel. User should feel like the app is clean and cutting edge.

The current demo is to display functionality only, we are hoping for a complete redesign of the app.

```html
<!DOCTYPE html>
<html lang="en">
<head>
<meta charset="utf-8">
<title>Verda Fitness – Chat Screen</title>
<link rel="stylesheet" href="https://fonts.googleapis.com/css2?family=Roboto:wght@300;400;500;700&display=swap">
<style>
  :root {
    --bg: #ece5f8;
    --ink: #111111;
    --brand-blue: #1d5fc8;
    --header-blue: #1a5cc0;
    --header-dark: #134aa3;
    --bubble-out: #2196f0;
    --bubble-in: #d8d8d8;
    --chat-bg: #f0f0f0;
    --muted: #666a70;
    --stamp: #9a9a9a;
    --text-in: #333333;
    --white: #ffffff;
    --outline: #55556a;
    --avatar: #5c4a3a;
    --avatar-2: #8fb8a8;
  }
  * { box-sizing: border-box; margin: 0; padding: 0; }
  html, body { width: 1200px; height: 1000px; overflow: hidden; }
  body {
    background: var(--bg);
    font-family: "Roboto", "Helvetica Neue", Arial, sans-serif;
    position: relative;
  }

  .project-info { position: absolute; left: 68px; top: 76px; }
  .project-title { font-size: 36px; font-weight: 300; color: var(--brand-blue); line-height: 1.1; }
  .project-tags { font-size: 22px; font-weight: 400; color: var(--muted); margin-top: 10px; }

  .screen-label {
    position: absolute; left: 770px; top: 841px; width: 364px; height: 79px;
    border: 2px solid var(--outline); border-radius: 6px;
    display: flex; align-items: center; justify-content: center;
    font-size: 38px; font-weight: 300; color: #3e3e4e;
  }

  .chat-screen {
    position: absolute; left: 420px; top: 190px; width: 340px; height: 604px;
    background: var(--chat-bg); overflow: hidden;
    box-shadow: 0 20px 50px rgba(60, 40, 110, 0.18);
    display: flex; flex-direction: column;
  }

  .app-header { background: var(--header-blue); color: var(--white); }
  .status-bar {
    height: 22px; display: flex; align-items: center; justify-content: space-between;
    padding: 0 8px; font-size: 12px;
  }
  .status-carrier { display: flex; align-items: center; gap: 5px; }
  .status-battery { display: flex; align-items: center; gap: 4px; }
  .nav-bar { height: 46px; position: relative; display: flex; align-items: center; justify-content: center; }
  .back-button {
    position: absolute; left: 8px; top: 6px; width: 34px; height: 34px; border-radius: 50%;
    background: var(--header-dark); display: flex; align-items: center; justify-content: center;
  }
  .contact-name { font-size: 17px; font-weight: 700; letter-spacing: 0.5px; }

  .message-list { flex: 1; padding: 16px 14px 0; display: flex; flex-direction: column; gap: 14px; }
  .timestamp { text-align: center; font-size: 10px; color: var(--stamp); text-transform: uppercase; letter-spacing: 0.3px; }

  .message { display: flex; align-items: flex-start; gap: 10px; }
  .message.outgoing { justify-content: flex-end; }
  .avatar {
    width: 38px; height: 38px; border-radius: 50%; flex: none;
    background: radial-gradient(circle at 50% 40%, var(--avatar-2), var(--avatar) 70%);
    border: 2px solid var(--white);
  }
  .bubble {
    position: relative; font-size: 13px; line-height: 1.35; padding: 9px 12px; max-width: 200px;
  }
  .incoming .bubble { background: var(--bubble-in); color: var(--text-in); margin-top: 14px; }
  .incoming .bubble::before {
    content: ""; position: absolute; left: 10px; top: -8px;
    border-left: 8px solid transparent; border-right: 8px solid transparent;
    border-bottom: 8px solid var(--bubble-in);
  }
  .outgoing .bubble { background: var(--bubble-out); color: var(--white); margin-right: 4px; }
  .outgoing .bubble::after {
    content: ""; position: absolute; right: 10px; bottom: -8px;
    border-left: 8px solid transparent; border-right: 8px solid transparent;
    border-top: 8px solid var(--bubble-out);
  }

  .compose-bar { height: 54px; background: var(--white); display: flex; align-items: stretch; }
  .compose-field { flex: 1; display: flex; align-items: center; gap: 12px; padding: 0 14px; font-size: 15px; color: #8a8a8a; }
  .compose-add { color: var(--brand-blue); font-size: 24px; font-weight: 300; }
  .send-button { width: 62px; background: var(--brand-blue); display: flex; align-items: center; justify-content: center; }
</style>
</head>
<body>
  <header class="project-info">
    <h1 class="project-title">VERDA FITNESS App Design</h1>
    <p class="project-tags">light theme, minimal, clean</p>
  </header>

  <main class="chat-screen">
    <div class="app-header">
      <div class="status-bar">
        <span class="status-carrier">●●●○○ Nova
          <svg width="13" height="10" viewBox="0 0 13 10"><path d="M1 3.5a8 8 0 0 1 11 0M3 5.7a5 5 0 0 1 7 0M5 7.9a2 2 0 0 1 3 0" fill="none" stroke="#fff" stroke-width="1.4"/></svg>
        </span>
        <span class="status-time">7:28 PM</span>
        <span class="status-battery">100%
          <svg width="24" height="11" viewBox="0 0 24 11"><rect x="0.5" y="0.5" width="20" height="10" rx="2" fill="none" stroke="#fff"/><rect x="2" y="2" width="17" height="7" fill="#fff"/><rect x="21.5" y="3.5" width="2" height="4" fill="#fff"/></svg>
        </span>
      </div>
      <nav class="nav-bar">
        <div class="back-button">
          <svg width="12" height="12" viewBox="0 0 12 12"><path d="M8 1.5 3.5 6 8 10.5" fill="none" stroke="#fff" stroke-width="1.6"/></svg>
        </div>
        <h2 class="contact-name">MARCO D</h2>
      </nav>
    </div>

    <section class="message-list">
      <p class="timestamp">March 26 @ 5:45 PM</p>
      <div class="message incoming">
        <div class="avatar" role="img" aria-label="Trainer profile photo"></div>
        <p class="bubble">Incoming Message Content + message line 1</p>
      </div>
      <div class="message outgoing">
        <p class="bubble">Outgoing Message Content + message line 1</p>
      </div>
      <div class="message incoming">
        <div class="avatar" role="img" aria-label="Trainer profile photo"></div>
        <p class="bubble">Incoming Message Content 2</p>
      </div>
      <p class="timestamp">4 minutes ago</p>
      <div class="message outgoing">
        <p class="bubble">Outgoing Message 2</p>
      </div>
      <div class="message incoming">
        <div class="avatar" role="img" aria-label="Trainer profile photo"></div>
        <p class="bubble">Incoming Message Content + message line 3</p>
      </div>
    </section>

    <footer class="compose-bar">
      <div class="compose-field"><span class="compose-add">+</span><span>Compose a message</span></div>
      <div class="send-button">
        <svg width="28" height="24" viewBox="0 0 28 24"><path d="M1 11 27 1 20 23 13 15Z" fill="#fff"/><path d="M13 15 27 1" stroke="#1d5fc8" stroke-width="1.2"/></svg>
      </div>
    </footer>
  </main>

  <div class="screen-label">Chat Screen</div>
</body>
</html>
```